Conference for Teenagers Needs Event Graphics

I am in need of event graphics for our upcoming event. This event, titled "Kestrel Youth Rally", is a weekend event for teenagers 11-19 years old. They hear from speakers, listen to a band, and do other fun activities. Our theme is "Together." Graphic design should have a young adult/older teen feel. Clean, not very bright colors.

Event Info:
November 6-8, 2020
Pellworth Exhibit Hall, Sioux Falls, SD
Speakers: TBD (will give name and picture before final approval)
Worship: (band name TBD before final approval)
KestrelYouthRally.com
#417KR
Our Organization Logo (attached): Lumen Forward

Once designed, I need the following graphics file sizes:
-11x17 Vertical Poster design: include all event info AND a "blank" spot/box for groups to add their own details/information. Also include the QRV logo and our organization logo Lumen Forward in someway.
-4x3 horizontal postcard: include all event info on 1 side including LumenForward logo and QRV; blank backside
-Main Graphic Slide: formatted to fit a widescreen 16x9 screen. Include event name, hashtag, QRV and Lumen Forward logo
-social media graphics for event: can incorporate some or all of the event details
-4.25x 2.75 vertical badge: include event title on front with Lumen Forward logo

Target Market(s)

Young adults or older teenagers

Requirements
Must have
• -event info
-Lumen Forward Logo & QRV logo

```html
<!DOCTYPE html>
<html lang="en">
<head>
<meta charset="utf-8">
<title>Kestrel Youth Rally – Poster</title>
<link rel="stylesheet" href="https://fonts.googleapis.com/css2?family=Montserrat:wght@600;700;800&family=Oswald:wght@400;500&display=swap">
<style>
  :root {
    --page-bg: #dcdcdc;
    --navy-deep: #040b33;
    --navy-mid: #0a1f6e;
    --navy-glow: #1236a8;
    --sky: #2ec4f4;
    --date-box: #1799cf;
    --title-shadow: #4a0a26;
    --white: #ffffff;
    --ink: #141414;
    --muted: #9aa3b5;
    --paper: #ffffff;
    --paper-shade: #ececec;
  }
  * { margin: 0; padding: 0; box-sizing: border-box; }
  html, body {
    width: 960px; height: 1200px; overflow: hidden;
    background: var(--page-bg);
  }
  .poster {
    position: absolute; left: 111px; top: 30px;
    width: 738px; height: 1140px;
    background: linear-gradient(180deg, var(--paper) 0%, var(--paper-shade) 100%);
    overflow: hidden;
    font-family: "Montserrat", sans-serif;
    color: var(--white);
  }
  .hero {
    position: absolute; left: 0; top: 0; width: 100%; height: 918px;
    background:
      radial-gradient(ellipse at 70% 95%, rgba(40,90,220,.55) 0%, rgba(40,90,220,0) 55%),
      radial-gradient(ellipse at 30% 60%, rgba(25,60,180,.45) 0%, rgba(25,60,180,0) 60%),
      linear-gradient(180deg, var(--navy-deep) 0%, var(--navy-mid) 55%, var(--navy-glow) 100%);
  }
  .org-name {
    position: absolute; left: 0; width: 100%; top: 140px;
    text-align: center;
    font-weight: 800; font-size: 62px; line-height: 64px;
    color: var(--sky); letter-spacing: 1px;
  }
  .title-frame {
    position: absolute; left: 61px; top: 388px; width: 615px; height: 148px;
    border: 1.5px solid var(--white); border-top: none;
  }
  .title-frame::before, .title-frame::after {
    content: ""; position: absolute; top: 0; width: 24px; height: 1.5px; background: var(--white);
  }
  .title-frame::before { left: 0; }
  .title-frame::after { right: 0; }
  .event-name {
    position: absolute; left: 0; width: 100%;
    text-align: center; font-family: "Oswald", sans-serif; text-transform: uppercase;
  }
  .event-name--lead {
    top: 330px; font-weight: 500; font-size: 108px; line-height: 126px;
    color: var(--sky); letter-spacing: 2px;
    text-shadow: -3px -2px 0 var(--title-shadow);
  }
  .event-name--sub {
    top: 443px; font-weight: 500; font-size: 74px; line-height: 84px;
    color: var(--white); letter-spacing: 1px;
  }
  .event-date {
    position: absolute; left: 0; width: 100%; top: 570px;
    display: flex; justify-content: center; align-items: center; gap: 20px;
    font-family: "Oswald", sans-serif; font-weight: 500; font-size: 70px; line-height: 76px;
  }
  .event-date__days {
    background: var(--date-box); padding: 0 12px; line-height: 66px; height: 66px;
  }
  .venue {
    position: absolute; left: 0; width: 100%; top: 659px;
    text-align: center; font-weight: 700; font-size: 22px; letter-spacing: 1.4px;
  }
  .lineup {
    position: absolute; top: 730px; width: 220px; text-align: center;
  }
  .lineup--speakers { left: 67px; }
  .lineup--worship { left: 445px; }
  .lineup__label {
    font-weight: 700; font-size: 17px; letter-spacing: 1px; color: var(--sky);
  }
  .lineup__value {
    font-weight: 800; font-size: 58px; line-height: 58px; margin-top: 2px; letter-spacing: 1px;
  }
  .portrait {
    position: absolute; top: 818px; width: 178px; height: 178px; border-radius: 50%;
    border: 2px solid var(--white);
  }
  .portrait--speaker {
    left: 88px;
    background: radial-gradient(circle at 45% 55%, #c23a3a 0%, #6a1e22 40%, #0b0b0b 75%);
  }
  .portrait--worship {
    left: 466px;
    background: radial-gradient(circle at 50% 45%, #c76a8c 0%, #5a3a8a 45%, #2b2650 80%);
  }
  .group-details {
    position: absolute; left: 292px; top: 934px; width: 154px; height: 104px;
    border: 1.5px dashed var(--muted);
  }
  .person-name {
    position: absolute; top: 1012px; width: 220px; text-align: center;
    font-weight: 700; font-size: 17px; letter-spacing: 1.2px; color: var(--ink);
  }
  .person-name--speaker { left: 67px; }
  .person-name--worship { left: 445px; }
  .footer {
    position: absolute; left: 40px; right: 40px; top: 1078px; height: 26px;
    display: flex; justify-content: space-between; align-items: center;
    font-weight: 600; font-size: 16px; letter-spacing: 1.6px; color: var(--ink);
  }
  .footer__hashtag { width: 130px; color: var(--date-box); font-weight: 700; }
  .footer__partner {
    width: 130px; display: flex; justify-content: flex-end; align-items: center; gap: 8px;
    font-weight: 700;
  }
  .footer__partner-square { width: 14px; height: 14px; background: var(--date-box); }
</style>
</head>
<body>
  <main class="poster">
    <section class="hero">
      <div class="org-name">LUMEN<br>FORWARD</div>

      <div class="title-frame"></div>
      <h1 class="event-name event-name--lead">Kestrel</h1>
      <h2 class="event-name event-name--sub">Youth Rally</h2>

      <div class="event-date">
        <span class="event-date__month">NOVEMBER</span>
        <span class="event-date__days">6-8</span>
        <span class="event-date__year">2020</span>
      </div>
      <p class="venue">PELLWORTH EXHIBIT HALL, SIOUX FALLS, SD</p>

      <div class="lineup lineup--speakers">
        <div class="lineup__label">SPEAKERS</div>
        <div class="lineup__value">TBD</div>
      </div>
      <div class="lineup lineup--worship">
        <div class="lineup__label">WORSHIP</div>
        <div class="lineup__value">TBD</div>
      </div>
    </section>

    <div class="portrait portrait--speaker" role="img" aria-label="Portrait photo of the speaker holding a microphone"></div>
    <div class="portrait portrait--worship" role="img" aria-label="Photo of the worship leader singing into a microphone"></div>

    <div class="group-details" aria-label="Space for group details"></div>

    <p class="person-name person-name--speaker">YOUR NAME</p>
    <p class="person-name person-name--worship">YOUR NAME</p>

    <footer class="footer">
      <span class="footer__hashtag">#417KR</span>
      <span class="footer__site">www.KestrelYouthRally.com</span>
      <span class="footer__partner"><span class="footer__partner-square"></span>QRV</span>
    </footer>
  </main>
</body>
</html>
```